Business cards Dorn Kelterhof GmbH & Co.KG

We need a uniform business card design template for our employees.
A template should be created to have the same design for all business cards.

Contact Information for Business Card

Firma und Firmierung, Name, Funktion in Unternehmen, Anschrift, Tel. Handynummer, Emailadresse, Internetseite

Colors

Designer to choose colors to be used in the design.

Requirements
Must have
• Our company logo must be on it

```html
<!DOCTYPE html>
<html lang="de">
<head>
<meta charset="utf-8">
<title>Visitenkarte – Dorn Kelterhof GmbH &amp; Co.KG</title>
<link rel="stylesheet" href="https://fonts.googleapis.com/css2?family=Arimo:wght@400&display=swap">
<style>
  :root {
    --canvas: #ffffff;
    --card-edge: #d9d9d9;
    --rust: #c8522a;
    --mid-brown: #7a2f1f;
    --espresso: #1e0f0f;
    --ink: #211011;
    --label: #ffffff;
  }
  html, body {
    margin: 0;
    padding: 0;
    width: 1200px;
    height: 1200px;
    overflow: hidden;
    background: var(--canvas);
    font-family: "Arimo", Arial, sans-serif;
  }
  .canvas {
    position: relative;
    width: 1200px;
    height: 1200px;
  }
  .business-card {
    position: absolute;
    left: 88px;
    top: 244px;
    width: 1028px;
    height: 588px;
    background: var(--canvas);
    outline: 1px solid var(--card-edge);
  }
  .contact-panel {
    position: absolute;
    left: 514px;
    top: 0;
    width: 514px;
    height: 588px;
    background: linear-gradient(90deg, var(--rust) 0%, var(--mid-brown) 35%, #3a1a15 70%, var(--espresso) 100%);
  }
  .hexagon {
    position: absolute;
    left: 462px;
    top: 233px;
    width: 104px;
    height: 122px;
  }
  .brand-name {
    position: absolute;
    left: 92px;
    top: 246px;
    margin: 0;
    font-size: 48px;
    font-weight: 400;
    line-height: 1;
    color: var(--ink);
    white-space: nowrap;
  }
  .field-label {
    position: absolute;
    left: 528px;
    margin: 0;
    font-size: 24px;
    line-height: 24px;
    color: var(--label);
    white-space: nowrap;
  }
  .field-name      { top: 33px; }
  .field-role      { top: 116px; }
  .field-address   { top: 198px; left: 526px; }
  .field-phone     { top: 372px; }
  .field-mobile    { top: 428px; }
  .field-email     { top: 484px; }
  .field-web       { top: 539px; }
</style>
</head>
<body>
<main class="canvas">
  <section class="business-card" aria-label="Visitenkarte Dorn Kelterhof GmbH &amp; Co.KG">
    <p class="brand-name">Dorn Kelterhof</p>

    <div class="contact-panel"></div>

    <svg class="hexagon" viewBox="0 0 104 122" aria-hidden="true">
      <polygon points="52,0 0,30 0,92 52,122" fill="var(--rust)"/>
      <polygon points="52,0 104,30 104,92 52,122" fill="#ffffff"/>
    </svg>

    <p class="field-label field-name">Name :</p>
    <p class="field-label field-role">Funktion in Unternehmen :</p>
    <p class="field-label field-address">Anschrift :</p>
    <p class="field-label field-phone">Tel :</p>
    <p class="field-label field-mobile">Handynummer :</p>
    <p class="field-label field-email">Emailadresse :</p>
    <p class="field-label field-web">Internetseite :</p>
  </section>
</main>
</body>
</html>
```